we do all sorts of cleaning however bookings are limited!
why not chose the right cleaners for you!
pressure cleaning, window cleaning, office, end of lease clean, accommodation, industrial and commercial cleaning and house cleaning

Logo Text

Bright Nest Cleaning Service

```html
<!DOCTYPE html>
<html lang="en">
<head>
<meta charset="UTF-8">
<title>Bright Nest Cleaning Service – Business Card</title>
<link href="https://fonts.googleapis.com/css2?family=Montserrat:wght@400;600;800&display=swap" rel="stylesheet">
<style>
  :root {
    --backdrop: #3a3a3a;
    --card-dark: #0b0b0b;
    --card-light: #ffffff;
    --brand-blue: #1aa3e8;
    --brand-green: #7dc242;
    --ink: #1c1c1c;
    --ink-soft: #4a4a4a;
  }
  * { margin: 0; padding: 0; box-sizing: border-box; }
  html, body {
    width: 1200px; height: 800px; overflow: hidden;
    background: var(--backdrop);
    font-family: "Montserrat", Arial, sans-serif;
  }
  .canvas {
    position: relative; width: 1200px; height: 800px;
    display: flex; align-items: center; justify-content: center; gap: 60px;
  }
  .card {
    position: relative; width: 500px; height: 286px;
    border-radius: 22px; overflow: hidden;
    box-shadow: 0 18px 40px rgba(0,0,0,0.35);
  }
  .card--back {
    background: var(--card-dark);
    display: flex; align-items: center; justify-content: center;
  }
  .brand-name {
    display: flex; align-items: center; gap: 10px;
    font-weight: 800; color: var(--brand-blue); line-height: 1.1;
  }
  .brand-name__dot {
    width: 14px; height: 14px; border-radius: 50%; background: var(--brand-green); flex: none;
  }
  .card--back .brand-name { font-size: 30px; }
  .card--back .brand-name__text { max-width: 290px; }

  .card--front { background: var(--card-light); }
  .card--front .brand-name {
    position: absolute; left: 34px; top: 170px; font-size: 18px;
  }
  .card--front .brand-name__text { max-width: 170px; }
  .contact {
    position: absolute; left: 250px; top: 36px; right: 20px;
  }
  .contact__name {
    font-size: 28px; font-weight: 800; color: var(--brand-blue); letter-spacing: -0.3px;
  }
  .contact__role {
    font-size: 12px; color: var(--ink-soft); margin-top: 2px; margin-bottom: 14px;
  }
  .contact__list { list-style: none; }
  .contact__item {
    display: flex; align-items: flex-start; gap: 10px;
    font-size: 13px; color: var(--ink); margin-bottom: 7px; line-height: 1.3;
  }
  .contact__icon {
    width: 20px; height: 20px; border-radius: 4px; background: var(--brand-blue);
    flex: none; display: flex; align-items: center; justify-content: center;
  }
  .contact__icon svg { width: 12px; height: 12px; }
  .card-band {
    position: absolute; left: 0; right: 0; bottom: 0; height: 12px; display: flex;
  }
  .card-band__blue { flex: 0 0 62%; background: var(--brand-blue); }
  .card-band__green { flex: 1; background: var(--brand-green); }
</style>
</head>
<body>
<main class="canvas">
  <section class="card card--back" aria-label="Card back">
    <div class="brand-name">
      <span class="brand-name__dot"></span>
      <span class="brand-name__text">Bright Nest Cleaning Service</span>
    </div>
  </section>

  <section class="card card--front" aria-label="Card front">
    <div class="brand-name">
      <span class="brand-name__dot"></span>
      <span class="brand-name__text">Bright Nest Cleaning Service</span>
    </div>

    <div class="contact">
      <h1 class="contact__name">Marcus Hale</h1>
      <p class="contact__role">Founder &amp; CEO</p>
      <ul class="contact__list">
        <li class="contact__item">
          <span class="contact__icon"><svg viewBox="0 0 24 24" fill="#fff"><path d="M6.6 10.8a15 15 0 0 0 6.6 6.6l2.2-2.2a1 1 0 0 1 1-.25 11.4 11.4 0 0 0 3.6.57 1 1 0 0 1 1 1V20a1 1 0 0 1-1 1A17 17 0 0 1 3 4a1 1 0 0 1 1-1h3.5a1 1 0 0 1 1 1c0 1.25.2 2.45.57 3.57a1 1 0 0 1-.25 1z"/></svg></span>
          <span>044-987 654 321</span>
        </li>
        <li class="contact__item">
          <span class="contact__icon"><svg viewBox="0 0 24 24" fill="#fff"><path d="M2 21l21-9L2 3v7l15 2-15 2z"/></svg></span>
          <span>hello@brightnestmail.com</span>
        </li>
        <li class="contact__item">
          <span class="contact__icon"><svg viewBox="0 0 24 24" fill="none" stroke="#fff" stroke-width="2"><circle cx="12" cy="12" r="9"/><path d="M3 12h18M12 3c3 3.5 3 14.5 0 18M12 3c-3 3.5-3 14.5 0 18"/></svg></span>
          <span>www.brightnestclean.com</span>
        </li>
        <li class="contact__item">
          <span class="contact__icon"><svg viewBox="0 0 24 24" fill="#fff"><path d="M12 2a7 7 0 0 0-7 7c0 5 7 13 7 13s7-8 7-13a7 7 0 0 0-7-7zm0 9.5A2.5 2.5 0 1 1 12 6.5a2.5 2.5 0 0 1 0 5z"/></svg></span>
          <span>4417 Harbor View Blvd<br>210-B, FL 32541</span>
        </li>
      </ul>
    </div>

    <div class="card-band">
      <span class="card-band__blue"></span>
      <span class="card-band__green"></span>
    </div>
  </section>
</main>
</body>
</html>
```